Completely Coded Dog Community Website - Mobile Centric & Highly Responsive

We need a completely coded design based in Wordpress CMS that is designed with mobile in mind first! I would like to carry over the style of our current website (brightkennels.c0m) into the design of the responsive website. In addition, please only submit designs if you provide high quality admin support, as the winning design will likely be hired to provide monthly support forward at $100/month (SEO skill set valued). Also am looking for a quote on an iphone and android app so please submit designs only if you have capability to create the highest quality apps. No cheap looking template submissions please...will need form, chat, sign in and e-commerce integration. I have vector files if needed for website.
Updates

Project Deadline Extended
Reason: Want to see more mobile friendly, modern designs and responses to willingness for web admin support going forward. Thanks

Target Market(s)

Adults based in the USA aged 25-50 that own dogs

Industry/Entity Type

E-Commerce

Requirements
Must have
• Pages:
Home Page
About Us
Contact Us
Dog Deals
Videos
Photos
Health
Training
Breeds
Ask the Dog Expert
Dog Product Reviews
Dog Stories
Dog Friendly Travel
Dog Care
Contests
Nice to have
• SEO
Metatags
Unique page layouts
Social integration to our social media accounts
Social API logins
Should not have
• Cheap template look
Not consistent with previous color scheme
Different logo than our current options

```html
<!DOCTYPE html>
<html lang="en">
<head>
<meta charset="utf-8">
<title>BrightKennels.com – Dog Community</title>
<link href="https://fonts.googleapis.com/css2?family=Open+Sans:wght@400;600;700&display=swap" rel="stylesheet">
<style>
:root{
  --teal:#367487;
  --orange:#f7a033;
  --text:#3a3a3a;
  --grey-icon:#8a8a8a;
  --footer:#222222;
  --footer-bottom:#1a1a1a;
  --footer-text:#a9a9a9;
  --white:#ffffff;
}
*{box-sizing:border-box;margin:0;padding:0}
html,body{width:1200px;height:2217px;overflow:hidden}
body{font-family:'Open Sans',sans-serif;color:var(--text);background:var(--white);position:relative}
.abs{position:absolute}
a{color:inherit;text-decoration:none}

/* header */
.brand{left:45px;top:40px;display:flex;align-items:center;gap:12px}
.brand-dot{width:46px;height:46px;border-radius:50%;background:var(--orange)}
.brand-name{font-size:32px;font-weight:700;color:var(--teal);letter-spacing:-.5px}
.call{left:706px;top:34px;display:flex;gap:10px;align-items:flex-start}
.call small{display:block;font-size:12px;font-weight:600;color:var(--teal)}
.call strong{display:block;font-size:20px;font-weight:400;color:#444}
.btn{display:flex;align-items:center;justify-content:center;color:var(--white);font-size:14px;font-weight:600;white-space:nowrap}
.btn-register{left:907px;top:38px;width:112px;height:31px;background:var(--orange)}
.btn-login{left:1028px;top:38px;width:111px;height:31px;background:var(--teal)}
.top-nav{right:60px;top:101px;display:flex;gap:30px;font-size:13.5px;color:#444;white-space:nowrap}

/* category bar */
.cat-bar{left:0;top:145px;width:1200px;height:44px;background:var(--teal);display:flex;padding-left:59px;font-size:13px;color:var(--white);white-space:nowrap}
.cat-bar a{display:flex;align-items:center;padding:0 21px}
.cat-bar a.active{background:var(--orange);color:#333;padding:0 30px}

/* hero */
.hero{left:0;top:189px;width:1200px;height:523px;background:radial-gradient(ellipse at 78% 45%,#f1ede4 0,#d8ccb2 16%,rgba(160,130,70,0) 34%),linear-gradient(180deg,#8b7232 0%,#a18744 45%,#6f7a3c 100%)}
.hero-copy{left:106px;top:381px;width:500px;color:var(--white)}
.hero-copy h1{font-size:21px;font-weight:400;margin-bottom:20px}
.hero-copy h1 b{font-weight:700}
.hero-copy p{font-size:14.5px;line-height:21px}
.hero-arrow{top:427px;width:30px;height:30px;border-radius:50%;background:rgba(255,255,255,.45);display:flex;align-items:center;justify-content:center}

/* welcome */
.welcome-title{left:62px;top:764px;font-size:20px;font-weight:400;color:#333;white-space:nowrap}
.welcome-text{left:62px;top:803px;width:615px;font-size:11.5px;line-height:18px;font-weight:600;color:#444;text-align:justify}
.avatar{left:60px;top:886px;width:153px;height:152px;background:#6cc4e6}
.intro-title{left:251px;top:885px;font-size:13.5px;font-weight:400;color:#333}
.intro-text{left:255px;top:918px;width:422px;font-size:11px;line-height:18px;color:#555;text-align:justify}
.btn-more{left:580px;top:1011px;width:98px;height:24px;background:var(--orange);font-size:12px;font-weight:400}
.video{left:705px;top:768px;width:434px;height:269px;border-radius:4px;border:2px solid #ddd;overflow:hidden;background:linear-gradient(160deg,#4d5a2c 0%,#7b8a4a 45%,#a8a68c 75%,#5e6a38 100%)}
.video-bar{left:0;bottom:0;width:100%;height:34px;background:#1c1c1c}

/* features */
.feature{top:1135px;width:279px;height:195px;text-align:center}
.feature svg{display:block;margin:8px auto 0}
.feature h3{font-size:17.5px;font-weight:400;color:#333;margin-top:14px;white-space:nowrap}
.feature p{font-size:13px;line-height:20px;color:#444;margin:2px auto 0;width:230px}
.divider{top:1135px;width:3px;height:195px;background:#eee}

/* newsletter */
.newsletter{left:58px;top:1399px;width:1082px;height:104px;background:var(--teal)}
.newsletter-title{left:92px;top:1435px;font-size:21px;font-weight:400;color:var(--white);white-space:nowrap}
.news-input{left:627px;top:1433px;width:265px;height:38px;background:var(--white);border-radius:2px;font-size:13px;color:#555;padding:9px 10px}
.btn-subscribe{left:904px;top:1433px;width:192px;height:38px;background:var(--orange);font-size:16px;letter-spacing:1px;border-radius:2px}

/* gallery */
.gallery-title{left:60px;top:1558px;font-size:22px;font-weight:400;color:#333}
.gallery-nav{left:1108px;top:1561px;display:flex;gap:6px}
.thumb{top:1605px;width:202px;height:161px}

/* footer */
.footer{left:0;top:1879px;width:1200px;height:276px;background:var(--footer)}
.footer-bottom{left:0;top:2155px;width:1200px;height:62px;background:var(--footer-bottom);color:#8a8a8a;font-size:11px;display:flex;align-items:center;justify-content:center}
.f-brand{left:60px;top:1925px;display:flex;align-items:center;gap:8px}
.f-brand span{font-size:17px;font-weight:700;color:#5fb8d6}
.f-brand i{width:24px;height:24px;border-radius:50%;background:var(--orange);display:block}
.f-about{left:60px;top:1990px;width:215px;font-size:11.5px;line-height:16px;color:var(--footer-text)}
.f-more{left:60px;top:2067px;width:203px;font-size:11.5px;color:var(--footer-text);display:flex;justify-content:space-between}
.f-social{left:60px;top:2097px;display:flex;gap:14px}
.f-social i{width:13px;height:13px;border-radius:50%;background:var(--white);display:block}
.f-head{top:1932px;font-size:12.5px;font-weight:700;letter-spacing:1px;color:var(--white)}
.f-head.soft{color:#8a8a8a;font-weight:600}
.f-links{left:394px;top:1962px;font-size:13px;line-height:22px;color:var(--footer-text);list-style:none}
.f-touch{left:615px;top:1960px;width:215px;font-size:12px;line-height:17px;color:var(--footer-text)}
.f-row{display:flex;gap:8px;align-items:flex-start;font-size:11.5px;margin-top:8px}
.f-row svg{flex:none;margin-top:3px}
.f-contact-text{left:925px;top:1960px;width:200px;font-size:11.5px;line-height:17px;color:#bbb}
.f-field{left:925px;width:212px;height:30px;background:#3a3a3a;border:1px solid #444;font-size:10px;color:#888;padding:8px 9px}
.btn-contact{left:1054px;top:2103px;width:82px;height:21px;background:var(--orange);font-size:11px;font-weight:400}
</style>
</head>
<body>

<header>
  <div class="abs brand"><span class="brand-dot"></span><span class="brand-name">BrightKennels.com</span></div>
  <div class="abs call">
    <svg width="18" height="30" viewBox="0 0 18 30"><path d="M4 2c2-1 4 0 4 2l1 5c0 2-1 3-3 3 0 4 2 7 4 9 1-1 3-2 4-1l3 3c1 1 1 3-1 4-3 2-7 1-10-3S0 12 1 6c0-2 1-3 3-4z" fill="var(--orange)"/></svg>
    <div><small>Call us on:</small><strong>0800 555 0142</strong></div>
  </div>
  <a class="abs btn btn-register" href="#">Register</a>
  <a class="abs btn btn-login" href="#">Login</a>
  <nav class="abs top-nav"><a href="#">Home</a><a href="#">About Us</a><a href="#">Contact Us</a><a href="#">Videos</a><a href="#">Breeds</a><a href="#">Contests</a></nav>
</header>

<nav class="abs cat-bar">
  <a class="active" href="#">Dog Deals</a><a href="#">Photos</a><a href="#">Health</a><a href="#">Training</a><a href="#">Ask the Dog Expert</a><a href="#">Dog Product Reviews</a><a href="#">Dog Stories</a><a href="#">Dog Friendly Travel</a><a href="#">Dog Care</a>
</nav>

<section class="abs hero" role="img" aria-label="Photo of a fluffy white puppy running on grass in warm blurred light"></section>
<div class="abs hero-copy">
  <h1><b>Contrary to</b> popular belief</h1>
  <p>reader will be distracted by the readable content of a page when looking at its layout. The point of using Lorem Ipsum is that it has a more-or-less normal distribution of letters, as opposed to using 'Content here, content here',</p>
</div>
<div class="abs hero-arrow" style="left:27px"><svg width="10" height="12"><path d="M8 1L2 6l6 5" stroke="#fff" stroke-width="2" fill="none"/></svg></div>
<div class="abs hero-arrow" style="left:1145px"><svg width="10" height="12"><path d="M2 1l6 5-6 5" stroke="#fff" stroke-width="2" fill="none"/></svg></div>

<section>
  <h2 class="abs welcome-title">WELCOME TO BRIGHT KENNELS</h2>
  <p class="abs welcome-text">Lorem ipsum dolor sit amet, consectetur adipiscing elit. Praesent sem urna, eleifend vel hendrerit non, tempus a nibh. Morbi tincidunt quis tortor vitae luctus. Phasellus euismod felis nec elit faucibus molestie. Proin tristique felis tortor, sit amet dictum leo viverra vitae.</p>
  <div class="abs avatar" role="img" aria-label="Cartoon dog mascot illustration"></div>
  <h3 class="abs intro-title">LOREM IPSUM DOLOR SIT</h3>
  <p class="abs intro-text">Ada Fenwick is a Learning Consultant and Facilitator who after over 15 successful years in sales &amp; marketing, turned to the world of education to facilitate individuals and teams towards personal and business success. As a Manager and Senior Learning Consultant at Northwind's Global Academy – Services division,</p>
  <a class="abs btn btn-more" href="#">Read More</a>
  <div class="abs video" role="img" aria-label="Video of a child walking a small dog along a park path">
    <div class="abs video-bar">
      <svg width="434" height="34" viewBox="0 0 434 34">
        <circle cx="22" cy="17" r="8" fill="none" stroke="#ddd" stroke-width="1.5"/><path d="M19 13l7 4-7 4z" fill="#ddd"/>
        <path d="M44 14h3l4-3v12l-4-3h-3z" fill="#ccc"/>
        <rect x="58" y="14" width="26" height="6" fill="#5fb8d6"/>
        <rect x="108" y="16" width="188" height="2" fill="#555"/><rect x="108" y="15" width="68" height="4" fill="#5fb8d6"/>
        <text x="310" y="21" font-size="9" fill="#ccc" font-family="Open Sans,sans-serif">01:30 / 04:55</text>
        <rect x="380" y="13" width="12" height="8" fill="none" stroke="#ccc"/>
        <circle cx="408" cy="17" r="5" fill="none" stroke="#ccc" stroke-width="2.5" stroke-dasharray="2 2"/>
      </svg>
    </div>
  </div>
</section>

<section>
  <div class="abs feature" style="left:36px">
    <svg width="54" height="50" viewBox="0 0 54 50"><path d="M27 48C10 34 2 26 2 15 2 7 8 2 15 2c5 0 9 3 12 7 3-4 7-7 12-7 7 0 13 5 13 13 0 11-8 19-25 33z" fill="var(--grey-icon)"/><g fill="#fff"><ellipse cx="27" cy="28" rx="7" ry="6"/><circle cx="18" cy="19" r="3"/><circle cx="24" cy="14" r="3"/><circle cx="30" cy="14" r="3"/><circle cx="36" cy="19" r="3"/></g></svg>
    <h3>DOG CARE</h3><p>Lorem Ipsum is simply dummy text of the printing and typesetting industry unknown printer.</p>
  </div>
  <div class="abs divider" style="left:313px"></div>
  <div class="abs feature" style="left:315px">
    <svg width="58" height="50" viewBox="0 0 58 50"><path d="M4 18C4 9 13 3 24 3s20 6 20 15-9 15-20 15c-3 0-5 0-7-1l-9 5 2-7C6 27 4 23 4 18z" fill="var(--grey-icon)"/><path d="M47 16c5 3 8 7 8 12 0 4-2 7-5 9l2 7-8-5c-2 1-4 1-6 1-8 0-14-4-17-9 15 0 25-7 26-15z" fill="var(--grey-icon)"/></svg>
    <h3>ASK THE DOG EXPERT</h3><p>Lorem Ipsum is simply dummy text of the printing and typesetting industry unknown printer.</p>
  </div>
  <div class="abs divider" style="left:592px"></div>
  <div class="abs feature" style="left:594px">
    <svg width="54" height="50" viewBox="0 0 54 50"><path d="M10 20a6 6 0 1 1 8-8l18 18a6 6 0 1 1-8 8L10 20z" fill="var(--grey-icon)" transform="translate(2 2)"/><circle cx="12" cy="13" r="6" fill="var(--grey-icon)"/><circle cx="42" cy="39" r="6" fill="var(--grey-icon)"/></svg>
    <h3>TRAINING</h3><p>Lorem Ipsum is simply dummy text of the printing and typesetting industry unknown printer.</p>
  </div>
  <div class="abs divider" style="left:870px"></div>
  <div class="abs feature" style="left:872px">
    <svg width="54" height="50" viewBox="0 0 54 50"><rect x="4" y="22" width="10" height="24" fill="var(--grey-icon)"/><path d="M17 22l9-12c2-4 4-8 6-8 3 0 4 3 3 7l-2 9h12c3 0 5 3 4 6l-4 18c-1 3-3 4-6 4H17z" fill="var(--grey-icon)"/></svg>
    <h3>DOG DEALS</h3><p>Lorem Ipsum is simply dummy text of the printing and typesetting industry unknown printer.</p>
  </div>
</section>

<section>
  <div class="abs newsletter"></div>
  <h2 class="abs newsletter-title">Join With us &amp; Subscribe for our free Newsletter</h2>
  <div class="abs news-input">Enter your email id</div>
  <a class="abs btn btn-subscribe" href="#">SUBSCRIBE</a>
</section>

<section>
  <h2 class="abs gallery-title">Our Gallery</h2>
  <div class="abs gallery-nav">
    <svg width="12" height="18"><path d="M10 2L3 9l7 7" stroke="var(--teal)" stroke-width="2.5" fill="none"/></svg>
    <svg width="12" height="18"><path d="M2 2l7 7-7 7" stroke="#999" stroke-width="2.5" fill="none"/></svg>
  </div>
  <div class="abs thumb" style="left:62px;background:linear-gradient(180deg,#d9d2c4,#7ea04a)" role="img" aria-label="Bulldog puppies on grass"></div>
  <div class="abs thumb" style="left:282px;background:linear-gradient(180deg,#86b43a,#d8c28e 60%,#6e9a2e)" role="img" aria-label="Golden puppy in a green garden"></div>
  <div class="abs thumb" style="left:501px;background:linear-gradient(180deg,#f2eee6,#e4cfa4 60%,#e048a0)" role="img" aria-label="Sleepy puppy in a pink basket"></div>
  <div class="abs thumb" style="left:720px;background:linear-gradient(160deg,#4d5a2c,#8c9a5c 50%,#a8a68c)" role="img" aria-label="Child walking a dog in a park"></div>
  <div class="abs thumb" style="left:940px;background:linear-gradient(180deg,#b0843e,#e8dcc4 50%,#9a7a3c)" role="img" aria-label="Golden retriever puppy running"></div>
</section>

<footer>
  <div class="abs footer"></div>
  <div class="abs f-brand"><i></i><span>BrightKennels.com</span></div>
  <p class="abs f-about">Magnis modipsae voloratati andigen daepeditem quiate re porem que aut labor. Laceaque eictemperum quiae sitiorem rest non</p>
  <div class="abs f-more"><span>More about us</span><span>→</span></div>
  <div class="abs f-social"><i></i><i></i><i></i><i></i></div>

  <h4 class="abs f-head" style="left:393px">USEFUL LINKS</h4>
  <ul class="abs f-links"><li>Home</li><li>About Us</li><li>Contact Us</li><li>Videos</li><li>Breeds</li><li>Contests</li></ul>

  <h4 class="abs f-head soft" style="left:615px">GET IN TOUCH</h4>
  <div class="abs f-touch">
    <p>Doloreiur quia commolu ptatemp dolupta orepreruum</p>
    <div class="f-row"><svg width="8" height="11"><path d="M4 11C1 7 0 5 0 4a4 4 0 0 1 8 0c0 1-1 3-4 7z" fill="#aaa"/></svg><span>Unit 4, Maple Court, 12 Harbour Lane, Leeds LS1 7QT</span></div>
    <div class="f-row"><svg width="8" height="11"><rect x="1" y="0" width="6" height="11" rx="1" fill="#aaa"/></svg><span>Phone : 020 7946 0321</span></div>
    <div class="f-row"><svg width="10" height="8"><rect x=".5" y=".5" width="9" height="7" fill="none" stroke="#aaa"/><path d="M.5 .5l4.5 4 4.5-4" fill="none" stroke="#aaa"/></svg><span>hello@yoursite.co.uk</span></div>
  </div>

  <h4 class="abs f-head" style="left:925px">CONTACT</h4>
  <p class="abs f-contact-text">Conecus iure posae volor remped modis</p>
  <div class="abs f-field" style="top:2007px">Email</div>
  <div class="abs f-field" style="top:2047px;display:flex;justify-content:space-between">Contact For<svg width="10" height="6"><path d="M1 1l4 4 4-4" stroke="#888" fill="none"/></svg></div>
  <a class="abs btn btn-contact" href="#">CONTACT</a>

  <div class="abs footer-bottom">© 2015 yoursite. All rights reserved.</div>
</footer>

</body>
</html>
```